I need creative and unique business card design using my company logo. Ok to change logo color. We are a small brokerage doing both Real Estate and Mortgage services. Need to have the follow on business card;
1. agent name - Nora Pelly - Realtor
2. cell - 555-281-4036
3. license number - DRE 07461392
4. business name - Brightfield Nest & Lending, Inc
5. business office - 555-730-1948
6. business address - 248 W. Marlowe Ave #312, Larkmoor CA 90471
7. business logo - attached (ok to use different color on logo)

```html
<!DOCTYPE html>
<html lang="en">
<head>
<meta charset="utf-8">
<title>Brightfield Nest &amp; Lending — Business Card</title>
<link rel="stylesheet" href="https://fonts.googleapis.com/css2?family=Montserrat:wght@400;500;700&display=swap">
<style>
  :root {
    --backdrop: #d3d6d7;
    --paper: #fbfbfb;
    --brand-blue: #2a5aa8;
    --deep-blue: #1f4a96;
    --ink: #2e2e33;
    --white: #ffffff;
  }
  * { box-sizing: border-box; margin: 0; padding: 0; }
  html, body { width: 1200px; height: 829px; overflow: hidden; }
  body {
    background: var(--backdrop);
    font-family: "Montserrat", Arial, sans-serif;
    position: relative;
  }
  .card {
    position: absolute;
    top: 260px;
    width: 540px;
    height: 309px;
    border-radius: 3px;
    box-shadow: 0 10px 28px rgba(0,0,0,.14);
  }
  .card--front { left: 40px; background: var(--paper); border-bottom: 3px solid var(--deep-blue); }
  .card--back { left: 620px; background: var(--brand-blue); }

  .brand {
    position: absolute;
    display: flex;
    flex-direction: column;
    align-items: center;
    text-align: center;
    font-weight: 500;
    letter-spacing: .32em;
    text-transform: uppercase;
  }
  .brand__square { display: block; margin-bottom: 14px; }
  .brand__name { line-height: 1.55; }

  .card--front .brand { left: 26px; top: 78px; width: 250px; color: var(--brand-blue); font-size: 11.5px; }
  .card--front .brand__square { width: 64px; height: 64px; background: var(--brand-blue); }

  .divider {
    position: absolute; left: 290px; top: 60px;
    width: 1px; height: 190px; background: var(--brand-blue);
  }

  .contact { position: absolute; left: 318px; top: 70px; right: 14px; color: var(--ink); font-size: 12.5px; line-height: 1.5; }
  .contact__name { font-weight: 700; font-size: 20px; color: var(--deep-blue); letter-spacing: .02em; text-transform: uppercase; }
  .contact__role { margin-bottom: 6px; }
  .contact__label { color: var(--brand-blue); }
  .contact__address { margin-bottom: 8px; }
  .contact__line { display: flex; align-items: center; gap: 7px; white-space: nowrap; }
  .contact__line svg { width: 11px; height: 11px; fill: var(--deep-blue); flex: none; }

  .card--back .brand { left: 0; right: 0; top: 86px; color: var(--white); font-size: 15px; }
  .card--back .brand__square { width: 88px; height: 88px; background: var(--white); opacity: .9; }
</style>
</head>
<body>
  <section class="card card--front" aria-label="Business card front">
    <div class="brand">
      <span class="brand__square"></span>
      <span class="brand__name">Brightfield<br>Nest &amp; Lending, Inc</span>
    </div>
    <div class="divider"></div>
    <div class="contact">
      <p class="contact__name">Nora Pelly</p>
      <p class="contact__role">Realtor</p>
      <p><span class="contact__label">Lic No</span> - DRE 07461392</p>
      <p class="contact__address">248 W. Marlowe Ave #312<br>Larkmoor CA 90471</p>
      <p class="contact__line">
        <svg viewBox="0 0 12 12" aria-hidden="true"><path d="M1 4c0-2 2-3 5-3s5 1 5 3v1H8V4H4v1H1zM3 6h6l2 4v1H1v-1z"/></svg>
        555-730-1948
      </p>
      <p class="contact__line">
        <svg viewBox="0 0 12 12" aria-hidden="true"><path d="M3.5 0h5a1 1 0 0 1 1 1v10a1 1 0 0 1-1 1h-5a1 1 0 0 1-1-1V1a1 1 0 0 1 1-1zm.5 1.5v8h4v-8z"/></svg>
        555-281-4036
      </p>
      <p class="contact__line">
        <svg viewBox="0 0 12 12" aria-hidden="true"><path d="M0 2h12v8H0zm1 1v.4l5 3.3 5-3.3V3z"/></svg>
        nora.pelly@brightfieldnest.net
      </p>
    </div>
  </section>

  <section class="card card--back" aria-label="Business card back">
    <div class="brand">
      <span class="brand__square"></span>
      <span class="brand__name">Brightfield<br>Nest &amp; Lending, Inc</span>
    </div>
  </section>
</body>
</html>
```